Heronvale Yards LLC - Door Hanger for Residential Mowing

Door Hanger- Heronvale Yards LLC. I would like the Heronvale Logo on a white background with three shades of pink incorporated into the flyer. Our phone number is 904-382-7046. And our website is heronvaleyardworks-example.com. I would like for the door hanger to mirror the Copperbend Door Hanger, using the Heronvale logo & information.

List of Services to include:
Pest Control
Termite Inspection
Lawn Maintenance
Debris Clean-up
Trash Removal
Home Inspection
Handy-man Services

Target Market(s)

Residential Lawns

Industry/Entity Type

Lawn Care

Font styles to use
Sans Serif

Colors
e34197
e667a6
eea4c8
f9d9e8

Requirements
Must have
• Phone Number
• Must be a Door Hanger
• Website
• 2 Sided
Nice to have
• 3 Shades of Pink with white background
Should not have
• It must be a door hanger. KEEP IN MIND THERE WILL BE A PUNCH HOLE AT TOP.......

```html
<!DOCTYPE html>
<html lang="en">
<head>
<meta charset="utf-8">
<title>Heronvale Pest Control – Door Hanger</title>
<link rel="stylesheet" href="https://fonts.googleapis.com/css2?family=Roboto:wght@300;400&family=Montserrat:wght@700&family=Lato:wght@400;700;900&display=swap">
<style>
  :root{
    --pink-strong:#e34197;
    --pink-mid:#e667a6;
    --pink-soft:#eea4c8;
    --pink-pale:#f9d9e8;
    --white:#ffffff;
    --ink:#3a3a3a;
    --page:#ecebea;
    --grass-dark:#3f8f1f;
    --grass-light:#8fd14f;
  }
  *{margin:0;padding:0;box-sizing:border-box}
  html,body{width:1200px;height:960px;overflow:hidden;background:var(--page)}
  .canvas{position:relative;width:1200px;height:960px}
  .hanger{position:absolute;top:124px;width:340px;height:712px;background:var(--white);overflow:hidden;box-shadow:0 2px 8px rgba(0,0,0,.18)}
  .hanger--front{left:245px}
  .hanger--back{left:615px}
  .hanger__backdrop{position:absolute;inset:0;width:340px;height:712px}
  .punch-hole{position:absolute;left:109px;top:34px;width:122px;height:122px;border-radius:50%;background:var(--page);box-shadow:inset 0 2px 4px rgba(0,0,0,.2)}
  .centered{position:absolute;left:0;width:100%;text-align:center}
  .brand-mark{position:absolute;left:140px;top:200px;width:60px;height:60px;border-radius:50%;background:var(--pink-mid)}
  .brand-name{font-family:"Roboto",sans-serif;font-weight:300;color:var(--pink-strong);font-size:26px;line-height:1}
  .front__name{top:340px}
  .headline{top:383px;font-family:"Montserrat",sans-serif;font-weight:700;font-size:14.5px;letter-spacing:1.4px;line-height:21px;color:var(--ink)}
  .price-pill{position:absolute;left:72px;top:448px;width:197px;height:51px;border:1.5px solid var(--pink-strong);border-radius:26px;background:var(--white)}
  .price-pill__sign{position:absolute;left:14px;top:9px;font-family:"Lato",sans-serif;font-weight:900;font-size:24px;color:var(--pink-strong)}
  .price-pill__unit{position:absolute;right:22px;bottom:8px;font-family:"Lato",sans-serif;font-weight:700;font-size:10px;color:var(--ink)}
  .fine-print{top:506px;font-family:"Lato",sans-serif;font-weight:700;font-size:12px;color:var(--ink)}
  .call-line{font-family:"Lato",sans-serif;font-weight:400;font-size:21px;color:var(--ink);line-height:1}
  .front__call{top:538px}
  .back__call{top:529px}
  .phone-band{position:absolute;left:0;width:100%;height:54px;background:var(--pink-strong);color:var(--white);font-family:"Lato",sans-serif;font-weight:900;font-size:40px;letter-spacing:3px;text-align:center;line-height:54px}
  .front__band{top:567px}
  .back__band{top:570px}
  .website{font-family:"Lato",sans-serif;font-weight:400;font-size:22px;color:var(--pink-strong);line-height:1}
  .front__web{top:634px}
  .back__web{top:637px}
  .grass{position:absolute;left:0;bottom:0;width:100%;height:50px;background:linear-gradient(180deg,var(--grass-light) 0%,var(--grass-dark) 100%)}
  .back__brand{position:absolute;top:196px;left:22px;display:flex;align-items:center;gap:12px}
  .back__brand .brand-square{width:22px;height:22px;border-radius:50%;background:var(--pink-mid)}
  .services__title{top:272px;font-family:"Lato",sans-serif;font-weight:900;font-size:22px;color:var(--pink-strong);line-height:1}
  .services__list{top:302px;list-style:none;font-family:"Lato",sans-serif;font-size:18.5px;color:#222;line-height:27.5px}
  .services__list li::before,.services__list li::after{content:"";display:inline-block;width:8px;height:8px;border-radius:50%;background:var(--pink-mid);vertical-align:middle;margin:0 14px}
</style>
</head>
<body>
<div class="canvas">

  <!-- Front side -->
  <section class="hanger hanger--front">
    <svg class="hanger__backdrop" viewBox="0 0 340 712" aria-hidden="true">
      <defs>
        <linearGradient id="front-glow" x1="0" y1="0" x2="0" y2="1">
          <stop offset="0" stop-color="#ffffff"/>
          <stop offset="1" stop-color="#eea4c8"/>
        </linearGradient>
      </defs>
      <rect width="340" height="712" fill="#fff"/>
      <polygon points="0,0 110,0 0,230" fill="#eea4c8" opacity=".6"/>
      <polygon points="0,0 60,0 0,120" fill="#e667a6" opacity=".35"/>
      <polygon points="340,0 230,0 340,230" fill="#eea4c8" opacity=".6"/>
      <polygon points="340,0 280,0 340,120" fill="#e667a6" opacity=".35"/>
      <polygon points="100,0 240,0 170,90" fill="#e667a6" opacity=".75"/>
      <rect x="0" y="400" width="340" height="170" fill="url(#front-glow)"/>
      <polygon points="0,430 80,567 0,567" fill="#e667a6" opacity=".35"/>
      <polygon points="340,430 260,567 340,567" fill="#e667a6" opacity=".35"/>
    </svg>
    <div class="punch-hole"></div>
    <div class="brand-mark"></div>
    <div class="centered brand-name front__name">Heronvale Pest Control</div>
    <div class="centered headline">Now Offering Lawn Care &amp; Home<br>Services In Your Neighborhood</div>
    <div class="price-pill">
      <span class="price-pill__sign">$</span>
      <span class="price-pill__unit">per service</span>
    </div>
    <div class="centered fine-print">No binding contract required</div>
    <div class="centered call-line front__call">Call to schedule service today</div>
    <div class="phone-band front__band">904-382-7046</div>
    <div class="centered website front__web">heronvaleyardworks-example.com</div>
    <div class="grass" role="img" aria-label="Strip of green lawn grass"></div>
  </section>

  <!-- Back side -->
  <section class="hanger hanger--back">
    <svg class="hanger__backdrop" viewBox="0 0 340 712" aria-hidden="true">
      <defs>
        <linearGradient id="back-glow" x1="0" y1="0" x2="0" y2="1">
          <stop offset="0" stop-color="#ffffff"/>
          <stop offset="1" stop-color="#eea4c8"/>
        </linearGradient>
      </defs>
      <rect width="340" height="712" fill="#fff"/>
      <polygon points="0,0 110,0 0,230" fill="#eea4c8" opacity=".6"/>
      <polygon points="0,0 60,0 0,120" fill="#e667a6" opacity=".35"/>
      <polygon points="340,0 230,0 340,230" fill="#eea4c8" opacity=".6"/>
      <polygon points="340,0 280,0 340,120" fill="#e667a6" opacity=".35"/>
      <polygon points="100,0 240,0 170,90" fill="#e667a6" opacity=".75"/>
      <rect x="0" y="380" width="340" height="190" fill="url(#back-glow)"/>
      <polygon points="0,300 90,570 0,570" fill="#e667a6" opacity=".35"/>
      <polygon points="340,300 250,570 340,570" fill="#e667a6" opacity=".35"/>
    </svg>
    <div class="punch-hole"></div>
    <div class="back__brand">
      <span class="brand-square"></span>
      <span class="brand-name">Heronvale Pest Control</span>
    </div>
    <div class="centered services__title">Services Available:</div>
    <ul class="centered services__list">
      <li>Pest Control</li>
      <li>Termite Inspection</li>
      <li>Lawn Maintenance</li>
      <li>Debris Clean-up</li>
      <li>Trash Removal</li>
      <li>Home Inspection</li>
      <li>Handy-man Services</li>
    </ul>
    <div class="centered call-line back__call">Call today for a free estimate</div>
    <div class="phone-band back__band">904-382-7046</div>
    <div class="centered website back__web">heronvaleyardworks-example.com</div>
    <div class="grass" role="img" aria-label="Strip of green lawn grass"></div>
  </section>

</div>
</body>
</html>
```